Brochure & Business card design

Looking for a new business card design i want it to be modern and sharp looking i usually order plastic business cards, and i would like to make the colors like the logo teal/charcoal i will like to have our services on icons with words.... our services are
ROOFING GUTTERS PAINTING PRESSURE WASHING EXTERIOR DESIGN & ATTIC VENTILATION. I also want to add my credentials

Target Market(s)

Oregon local market

Industry/Entity Type

Residential Construction

Contact Information for Business Card

Business info, services, number, website

Font styles to use
Serif
Sans Serif

Colors
33b8a4
5c5c5c
ffffff

Requirements
Must have
• Dale Finch
• Cell:
• Office:
• Email:
• Website:
• also i need our social media icons
• Services ROOFING GUTTERS PAINTING PRESSURE WASHING EXTERIOR DESIGN & ATTIC VENTILATION
• -icons for number, web, email, cell
• OR #584312
• Wa #KTRABLD461X7
Nice to have
• -Clean design Front & Back
• -Icons
• -shape House just like logo design
• -First Impression
Should not have
• Not Busy or lost of eye contact

```html
<!DOCTYPE html>
<html lang="en">
<head>
<meta charset="utf-8">
<title>Crestline Home Exteriors – Business Card</title>
<link href="https://fonts.googleapis.com/css2?family=Open+Sans:wght@400;600;700&family=Raleway:wght@300;400&display=swap" rel="stylesheet">
<style>
  :root{
    --teal:#33b8a4;
    --teal-deep:#1f9a88;
    --charcoal:#5c5c5c;
    --charcoal-dark:#3a3a3a;
    --white:#ffffff;
    --backdrop:#e6e6e6;
    --line:#d4d4d4;
  }
  *{box-sizing:border-box;margin:0;padding:0}
  html,body{width:1200px;height:856px;overflow:hidden;background:var(--backdrop)}
  .canvas{position:relative;width:1200px;height:856px}
  .card{position:absolute;top:270px;width:555px;height:317px;background:var(--white);
        border-radius:24px;overflow:hidden;box-shadow:0 6px 18px rgba(0,0,0,.12)}
  .card--contact{left:30px}
  .card--name{left:615px}

  /* contact side */
  .brand{position:absolute;display:flex;align-items:center;gap:10px;
         font-family:"Open Sans",sans-serif;font-weight:700;color:var(--teal-deep)}
  .brand__mark{width:18px;height:18px;background:var(--charcoal)}
  .card--contact .brand{left:40px;top:112px;font-size:19px;width:220px;line-height:1.2}
  .badge-accredited{position:absolute;left:40px;top:232px;width:120px;height:34px;
         border-radius:5px;background:var(--charcoal-dark)}
  .divider{position:absolute;left:250px;top:40px;width:170px;height:150px}
  .contact-list{position:absolute;left:318px;top:40px;list-style:none;
         font-family:"Open Sans",sans-serif;font-size:11.5px;color:var(--charcoal)}
  .contact-list li{display:flex;align-items:flex-start;gap:10px;margin-bottom:6px}
  .contact-list .address{color:var(--teal-deep);font-weight:700;line-height:1.4}
  .contact-list svg{flex:none;width:14px;height:14px;margin-top:1px}
  .badge-certified{position:absolute;right:26px;top:218px;width:96px;height:30px;
         border-radius:3px;background:#d8322f}
  .band-teal{position:absolute;left:0;bottom:40px;width:430px;height:8px;background:var(--teal)}
  .band-charcoal{position:absolute;right:0;bottom:40px;width:140px;height:14px;background:var(--charcoal);
         clip-path:polygon(8% 0,100% 0,100% 100%,0 100%)}

  /* name side */
  .roof-glow{position:absolute;left:90px;top:-40px;width:400px;height:230px;
         background:linear-gradient(180deg,#f1f1f1,#ffffff 80%)}
  .card--name .brand{left:0;right:0;top:92px;justify-content:center;font-size:22px}
  .services{position:absolute;left:0;right:0;top:180px;text-align:center;
         font-family:"Open Sans",sans-serif;font-size:10.5px;color:var(--teal-deep);letter-spacing:.2px}
  .services .dot{display:inline-block;width:5px;height:5px;border-radius:50%;
         background:var(--charcoal-dark);margin:0 4px 1px}
  .name-tab{position:absolute;right:0;top:216px;width:330px;height:40px;
         background:linear-gradient(180deg,var(--charcoal),var(--charcoal-dark));
         clip-path:polygon(4% 0,100% 0,100% 100%,0 100%);
         display:flex;align-items:center;justify-content:center;gap:8px;color:var(--white)}
  .name-tab__name{font-family:"Raleway",sans-serif;font-weight:300;font-size:21px}
  .name-tab__title{font-family:"Raleway",sans-serif;font-size:9px;letter-spacing:.5px}
  .band-base{position:absolute;left:0;right:0;bottom:0;height:40px;
         background:linear-gradient(180deg,#d9d9d9,#f4f4f4)}
</style>
</head>
<body>
<div class="canvas">

  <section class="card card--contact">
    <div class="brand"><span class="brand__mark"></span><span>Crestline Home Exteriors</span></div>
    <div class="badge-accredited" role="img" aria-label="Accreditation badge"></div>

    <svg class="divider" viewBox="0 0 170 150"><line x1="10" y1="10" x2="90" y2="145" stroke="#d4d4d4" stroke-width="2"/></svg>

    <ul class="contact-list">
      <li><svg viewBox="0 0 14 14"><circle cx="7" cy="7" r="7" fill="var(--teal)"/><path d="M7 3a2.5 2.5 0 0 0-2.5 2.5C4.5 7.5 7 11 7 11s2.5-3.5 2.5-5.5A2.5 2.5 0 0 0 7 3z" fill="#fff"/></svg>
        <span class="address">Example Alder, Suite 0000,<br>Salem, OR 97301</span></li>
      <li><svg viewBox="0 0 14 14"><circle cx="7" cy="7" r="7" fill="var(--teal)"/><path d="M4.5 4h1.6l.7 1.8-1 .7a5 5 0 0 0 1.7 1.7l.7-1 1.8.7v1.6c-3.5.2-5.7-2-5.5-5.5z" fill="#fff"/></svg>
        <span>(000) 000-5184</span></li>
      <li><svg viewBox="0 0 14 14"><circle cx="7" cy="7" r="7" fill="var(--teal)"/><rect x="3.5" y="4.5" width="7" height="5" fill="#fff"/><path d="M3.5 4.5 7 7.3l3.5-2.8" fill="none" stroke="var(--teal)" stroke-width=".8"/></svg>
        <span>contact@crestlinehomeexteriors.com</span></li>
      <li><svg viewBox="0 0 14 14"><circle cx="7" cy="7" r="7" fill="var(--teal)"/><circle cx="7" cy="7" r="3.6" fill="none" stroke="#fff" stroke-width=".9"/><path d="M3.4 7h7.2M7 3.4c-1.8 2-1.8 5.2 0 7.2M7 3.4c1.8 2 1.8 5.2 0 7.2" fill="none" stroke="#fff" stroke-width=".7"/></svg>
        <span>www.crestlinehomeexteriors.com</span></li>
      <li><svg viewBox="0 0 14 14"><circle cx="7" cy="7" r="7" fill="var(--teal)"/></svg>
        <span>@crestlinehomes</span></li>
      <li><svg viewBox="0 0 14 14"><circle cx="7" cy="7" r="7" fill="var(--teal)"/></svg>
        <span>@crestlinehomes</span></li>
    </ul>

    <div class="badge-certified" role="img" aria-label="Certification badge"></div>
    <div class="band-teal"></div>
    <div class="band-charcoal"></div>
  </section>

  <section class="card card--name">
    <div class="roof-glow" role="img" aria-label="Faint roof-shaped background decoration"></div>
    <div class="brand"><span class="brand__mark"></span><span>Crestline Home Exteriors</span></div>
    <p class="services"><span class="dot"></span>ROOFING GUTTERS PAINTING<span class="dot"></span>PRESSURE WASHING<span class="dot"></span>EXTERIOR DESIGN<span class="dot"></span>ATTIC VENTILATION</p>
    <div class="name-tab"><span class="name-tab__name">Dale Finch</span><span class="name-tab__title">DESIGNATION</span></div>
    <div class="band-base"></div>
  </section>

</div>
</body>
</html>
```